Tattoo Artist needs a personal business card designed

I am looking for a classy, clean, but antique feeling business card for myself that matches the theme and vibe of my tattoo shop. I would like to see a couple different options but we can go with an all black background, to start. I would like to see some western metallic lettering and deep/dark red accents. Maybe try adding a few with a mix of white fonts too. I would like to see the Shop's name and location which is Copper Lantern Ink, 4862 W. Delmora Rd. Tampa FL. 33617 Our tattoo shop has a western antique vibe, yet its classy and professional. We have a website you can see the color scheme and grab anymore information for designing this business card from: www.copperlanternink-studio.example - and if you want to add the website to the card. I would like my personal IG handle somewhere small with a unique and cleaner IG logo next to the name. My IG handle is: @dianekessoink I am basically trying to look for multiple ideas/concepts that will match best with our website and sticker. (Which I will upload in the files) I would like it to be very clean, simple, classy, but have a western traditional tattooing feel to it. Like an antique stores business card. Add whatever information you think would be best, since I am not the professional graphic designer.
Shop Name: Copper Lantern Ink
Location: 4862 W Delmora Rd Tampa FL 33617
Website: www.copperlanternink-studio.example
Number: 813 555 0187
My Personal IG: @dianekessoink

Thank you for taking your time to help me out with this project. Afterwards, I might need our studios website up for re-designing! So my end goal is to make everything intergraded with one another. I more likely need a logo too.

Target Market(s)

Professionals 35-55 years of age Male and Female
Firefighters, Military Service men and women

Contact Information for Business Card

All black background, with golden and red accents.
Traditional style, cowboy, western. Sharp, Clean, and Classy.

Requirements
Must have
• Shop Name - Copper Lantern Ink
• Shop Location - 4862 W Delmora Rd Tampa FL 33617
• My Name - Diane Kesso
• UNIQUE IG LOGO along with My Instagram - @dianekessoink
• Number - 813 555 0187
Nice to have
• Gold metallic font
• Red accents
• Western Antique Oddity feel
• Might be nice to have the Website if it can work and fit in the space.

```html
<!DOCTYPE html>
<html lang="en">
<head>
<meta charset="utf-8">
<title>Diane Kesso – Business Card</title>
<link href="https://fonts.googleapis.com/css2?family=Cinzel:wght@400;500&family=Lato:wght@400;700&display=swap" rel="stylesheet">
<style>
  :root {
    --backdrop: #6e3f1c;
    --card: #1f1f1f;
    --gold: #e0b44a;
    --red: #c8121b;
    --white: #ecebe8;
    --soft-white: #d6d6d6;
    --rule: #8d8d8d;
  }
  * { margin: 0; padding: 0; box-sizing: border-box; }
  html, body { width: 1200px; height: 900px; overflow: hidden; }
  body {
    background: var(--backdrop);
    font-family: "Lato", Arial, sans-serif;
    position: relative;
  }
  .card {
    position: absolute;
    left: 330px;
    width: 556px;
    height: 343px;
    background: var(--card);
    box-shadow: 2px 3px 6px rgba(0,0,0,0.45);
    text-align: center;
  }
  .card-front { top: 90px; }
  .card-back { top: 470px; }

  .holder-name {
    position: absolute;
    top: 99px; left: 0; right: 0;
    font-family: "Cinzel", Georgia, serif;
    font-weight: 400;
    font-size: 22px;
    letter-spacing: 1px;
    color: var(--gold);
  }
  .rule {
    position: absolute;
    left: 193px;
    width: 167px;
    height: 1px;
    background: var(--rule);
  }
  .rule-top { top: 133px; }
  .rule-bottom { top: 196px; }
  .contact {
    position: absolute;
    left: 0; right: 0;
    font-size: 16px;
    line-height: 20px;
    color: var(--white);
  }
  .contact .label { color: var(--gold); font-weight: 700; }
  .contact-phone { top: 143px; }
  .contact-web { top: 164px; }
  .shop-name, .shop-address {
    position: absolute;
    left: 0; right: 0;
    font-size: 16px;
    line-height: 20px;
    color: var(--soft-white);
  }
  .shop-name { top: 204px; }
  .shop-address { top: 225px; }

  .brand-mark {
    position: absolute;
    top: 78px;
    left: 228px;
    width: 100px;
    height: 100px;
    border: 3px solid var(--gold);
    border-radius: 50%;
  }
  .brand-name {
    position: absolute;
    top: 198px; left: 0; right: 0;
    font-family: "Cinzel", Georgia, serif;
    font-weight: 500;
    font-size: 36px;
    line-height: 44px;
    letter-spacing: 2px;
    color: var(--gold);
  }
  .instagram {
    position: absolute;
    top: 280px; left: 0; right: 0;
    font-size: 15px;
    line-height: 20px;
    font-weight: 700;
    color: var(--gold);
  }
  .instagram .label { color: var(--red); }
</style>
</head>
<body>
  <section class="card card-front">
    <h1 class="holder-name">DIANE KESSO</h1>
    <div class="rule rule-top"></div>
    <p class="contact contact-phone"><span class="label">P:</span> 813 555 0187</p>
    <p class="contact contact-web"><span class="label">W:</span> www.copperlanternink-studio.example</p>
    <div class="rule rule-bottom"></div>
    <p class="shop-name">Copper Lantern Ink</p>
    <p class="shop-address">4862 W Delmora Rd Tampa FL 33617</p>
  </section>

  <section class="card card-back">
    <div class="brand-mark"></div>
    <h2 class="brand-name">COPPER LANTERN INK</h2>
    <p class="instagram"><span class="label">InstaGram:</span> @dianekessoink</p>
  </section>
</body>
</html>
```